Business Card Design for new logo

Business card Design for new logo. Follow colors from logo.
The company has offices in multiple comtries
Want to have some bulltes on the countries and also on the main services

Something like
USA*Dominican Republic*LATAM

Consulting*Healthcare IT*Tranformation

Industry/Entity Type

Information Technology

Contact Information for Business Card

Address, Phones, countries, name and position

Miron castell

Founder and CEO

947 Quarry Ln
Mill haven, PA 16835

Mcastell@novelquin.com

www.novelquin.com

717-352-6081

828-444-4444

```html
<!DOCTYPE html>
<html lang="en">
<head>
<meta charset="utf-8">
<title>Novelquin Health – Business Card</title>
<link href="https://fonts.googleapis.com/css2?family=Marcellus&family=Roboto:wght@400&display=swap" rel="stylesheet">
<style>
  :root {
    --stage: #2b2b2b;
    --paper: #f7f7f6;
    --blue: #1f78b8;
    --orange: #e6783a;
    --ink: #2a2a2a;
    --muted: #3c3c3c;
  }
  * { margin: 0; padding: 0; box-sizing: border-box; }
  html, body { width: 1200px; height: 852px; overflow: hidden; }
  body { background: var(--stage); position: relative; font-family: "Roboto", Arial, sans-serif; }

  .card {
    position: absolute;
    width: 600px; height: 343px;
    left: 300px;
    background: var(--paper);
    border-radius: 22px;
    overflow: hidden;
  }
  .card--front { top: 62px; border-bottom: 8px solid var(--blue); }
  .card--back { top: 448px; }

  /* Front */
  .brand-lockup { position: absolute; top: 74px; left: 0; right: 0; text-align: center; }
  .brand-mark {
    display: inline-block; width: 30px; height: 30px; border-radius: 50%;
    background: var(--blue); vertical-align: middle; margin-right: 12px;
  }
  .brand-name {
    font-family: "Marcellus", Georgia, serif; color: var(--blue);
    font-size: 46px; vertical-align: middle;
  }
  .services {
    margin-top: 12px; font-size: 14px; color: var(--muted); letter-spacing: .3px;
  }
  .sep { color: var(--ink); margin: 0 6px; }
  .rule { position: absolute; height: 2px; background: var(--orange); }
  .rule--top { top: 200px; left: 390px; width: 70px; }
  .rule--bottom { top: 270px; left: 140px; width: 60px; }
  .countries {
    position: absolute; top: 226px; left: 0; right: 0; text-align: center;
    font-size: 15px; color: var(--muted);
  }
  .countries .sep { color: var(--orange); margin: 0 10px; }

  /* Back */
  .back-brand {
    position: absolute; top: 56px; left: 44px;
    font-family: "Marcellus", Georgia, serif; color: var(--blue); font-size: 40px;
  }
  .edge-dot {
    position: absolute; left: -22px; top: 188px; width: 44px; height: 44px;
    border-radius: 50%; background: var(--orange);
  }
  .person { position: absolute; top: 150px; left: 44px; }
  .person-name { font-family: "Marcellus", Georgia, serif; color: var(--blue); font-size: 24px; }
  .person-role { font-size: 14px; color: var(--ink); margin-top: 2px; }
  .contacts { position: absolute; top: 218px; left: 44px; list-style: none; }
  .contact { display: flex; align-items: center; height: 21px; font-size: 14px; color: var(--ink); }
  .contact svg { width: 13px; height: 13px; margin-right: 14px; fill: var(--orange); flex: none; }
  .contact--plain { padding-left: 0; }
</style>
</head>
<body>

<section class="card card--front">
  <div class="brand-lockup">
    <span class="brand-mark"></span><span class="brand-name">Novelquin Health</span>
    <p class="services">Consulting<span class="sep">|</span>Healthcare IT<span class="sep">|</span>Transformation</p>
  </div>
  <span class="rule rule--top"></span>
  <p class="countries">USA<span class="sep">|</span>Dominican Republic<span class="sep">|</span>LATAM</p>
  <span class="rule rule--bottom"></span>
</section>

<section class="card card--back">
  <div class="back-brand">Novelquin Health</div>
  <span class="edge-dot"></span>
  <div class="person">
    <p class="person-name">Miron castell</p>
    <p class="person-role">Founder &amp; CEO</p>
  </div>
  <ul class="contacts">
    <li class="contact">
      <svg viewBox="0 0 16 16" aria-hidden="true"><rect x="3" y="0" width="10" height="16" rx="2"/><rect x="5" y="2" width="6" height="10" fill="#f7f7f6"/></svg>
      717-352-6081
    </li>
    <li class="contact">
      <svg viewBox="0 0 16 16" aria-hidden="true"><path d="M1 5c0-2 3-3 7-3s7 1 7 3v1h-4V4H5v2H1zM3 8h10l2 7H1z"/></svg>
      828-444-4444
    </li>
    <li class="contact">
      <svg viewBox="0 0 16 16" aria-hidden="true"><rect x="0" y="3" width="16" height="10" rx="1"/><path d="M1 4l7 5 7-5" stroke="#f7f7f6" stroke-width="1.4" fill="none"/></svg>
      Mcastell@novelquin.com
    </li>
    <li class="contact">
      <svg viewBox="0 0 16 16" aria-hidden="true"><circle cx="8" cy="8" r="7.5"/><path d="M1 8h14M8 1v14M3 4h10M3 12h10" stroke="#f7f7f6" stroke-width="1" fill="none"/></svg>
      www.novelquin.com
    </li>
    <li class="contact contact--plain">947 Quarry Ln Mill haven, PA 16835</li>
  </ul>
</section>

</body>
</html>
```